Kestrel Ridgeway LLC stationery, business card and web page design.

i need a full set of stationery designed using the name "Kestrel Ridgeway LLC" with a tag line "construction consulting services". using the uploaded monkey icon as the logo.

i like the colors orange, green and black in general but im not limited to that. the company offers consulting services to various types of construction businesses.

Target Market(s)

i travel around the country in a 4x4 camper offering consulting services and technical training short term and long to various types of construction companies.

Industry/Entity Type

Construction Company

Contact Information for Business Card

Martin Hale
m.hale@kestrelridgeway.example
2475 Birchfield Rd
Bohemia, NY 11716
555 314 0627

list these services on the card.

Business Consulting
Capital Investments
Marketing Implementations
Technical Training

Number of Pages Required

1 page

Colors

Designer to choose colors to be used in the design.

Requirements
Must have
• company info and use of the monkey icon i provided.
Nice to have
• a fun but professional design
Should not have
• the color red

```html
<!DOCTYPE html>
<html lang="en">
<head>
<meta charset="utf-8">
<title>Kestrel Ridgeway LLC – Business Card</title>
<link href="https://fonts.googleapis.com/css2?family=Cinzel:wght@400;600&family=Open+Sans:wght@400;600&display=swap" rel="stylesheet">
<style>
  :root {
    --backdrop: #3a302c;
    --card: #1b1b1d;
    --card-edge: #26262a;
    --orange: #f0642a;
    --white: #f2f2f2;
    --grey: #9a9a9a;
    --mark-grey: #bdbdbd;
  }
  * { margin: 0; padding: 0; box-sizing: border-box; }
  html, body { width: 1200px; height: 864px; overflow: hidden; }
  body {
    background: var(--backdrop);
    position: relative;
    font-family: "Open Sans", sans-serif;
    color: var(--white);
  }
  .card {
    position: absolute;
    background: linear-gradient(160deg, var(--card-edge), var(--card) 60%);
    border-radius: 4px;
    box-shadow: 0 14px 30px rgba(0,0,0,.45);
    overflow: hidden;
  }
  /* Back of card */
  .card-back { left: 60px; top: 110px; width: 520px; height: 300px; }
  .brand-mark {
    position: absolute;
    display: flex; align-items: center; gap: 10px;
    font-family: "Open Sans", sans-serif;
    font-weight: 600;
    white-space: nowrap;
  }
  .card-back .brand-mark {
    left: 50%; top: 92px; transform: translateX(-50%);
    font-size: 26px; color: var(--mark-grey);
  }
  .brand-dot { width: 22px; height: 22px; border-radius: 50%; background: var(--mark-grey); flex: none; }
  .back-url {
    position: absolute; left: 34px; bottom: 34px;
    font-size: 15px; letter-spacing: 7px; color: var(--grey);
  }
  /* Front of card */
  .card-front { left: 610px; top: 420px; width: 550px; height: 315px; }
  .identity {
    position: absolute; left: 0; top: 0; width: 280px; height: 100%;
    display: flex; flex-direction: column; align-items: center; justify-content: center;
  }
  .card-front .brand-mark {
    position: static; font-size: 17px; color: var(--white); margin-bottom: 26px;
  }
  .card-front .brand-dot { width: 16px; height: 16px; background: var(--white); }
  .company-name {
    font-family: "Cinzel", serif; font-size: 18px; color: var(--orange);
    letter-spacing: .4px; text-transform: uppercase; white-space: nowrap;
  }
  .tagline {
    font-family: "Cinzel", serif; font-size: 9px; color: var(--white);
    letter-spacing: .5px; text-transform: uppercase; margin-top: 2px; white-space: nowrap;
  }
  .divider {
    position: absolute; left: 286px; top: 40px; width: 1px; height: 235px;
    background: linear-gradient(to bottom, transparent, #cfcfcf 30%, #cfcfcf 70%, transparent);
  }
  .contact { position: absolute; left: 304px; top: 54px; width: 230px; font-size: 13px; line-height: 19px; }
  .person-name { color: var(--orange); font-weight: 600; font-size: 16px; text-transform: uppercase; }
  .person-title { font-size: 13px; margin-bottom: 12px; }
  .address { margin-bottom: 4px; }
  .contact-line { display: flex; align-items: center; gap: 7px; white-space: nowrap; }
  .contact-line svg { width: 11px; height: 11px; fill: var(--orange); flex: none; }
  .web { padding-left: 18px; }
</style>
</head>
<body>
  <section class="card card-back" aria-label="Business card, back">
    <div class="brand-mark"><span class="brand-dot"></span>Kestrel Ridgeway</div>
    <p class="back-url">www.kestrelridgeway.example</p>
  </section>

  <section class="card card-front" aria-label="Business card, front">
    <div class="identity">
      <div class="brand-mark"><span class="brand-dot"></span>Kestrel Ridgeway</div>
      <p class="company-name">Kestrel Ridgeway LLC</p>
      <p class="tagline">Construction Consulting Services</p>
    </div>
    <div class="divider"></div>
    <div class="contact">
      <p class="person-name">Martin Hale</p>
      <p class="person-title">CEO/FOUNDER</p>
      <p class="address">2475 Birchfield Rd<br>Bohemia, NY 11716</p>
      <p class="contact-line">
        <svg viewBox="0 0 12 12"><path d="M1 4c0-2 1-3 5-3s5 1 5 3v1H8V4H4v1H1zM2 6h8l1 5H1z"/></svg>555 314 0627
      </p>
      <p class="contact-line">
        <svg viewBox="0 0 12 12"><path d="M3 0h6a1 1 0 0 1 1 1v10a1 1 0 0 1-1 1H3a1 1 0 0 1-1-1V1a1 1 0 0 1 1-1zm0 2v7h6V2z"/></svg>555 314 0628
      </p>
      <p class="contact-line">
        <svg viewBox="0 0 12 12"><path d="M3 0h6v4H3zM1 5h10v6H1zm2 2v1h2V7z"/></svg>555 314 0629
      </p>
      <p class="contact-line">
        <svg viewBox="0 0 12 12"><circle cx="6" cy="6" r="6"/><path d="M3 4h6v4H3z" fill="#1b1b1d"/></svg>m.hale@kestrelridgeway.example
      </p>
      <p class="contact-line web">www.kestrelridgeway.example</p>
    </div>
  </section>
</body>
</html>
```